Book cover for a book on tactics, habits and directives learned from world class performers

The Quiet Ledger book is the first in a series of four books filled with proven tactics, habits and directives (i.e., what to do) that young, ambitious working professionals should be doing to make their life better. The first book is on foundational or keystone habits - that is, the habits that will help everyone upgrade their life and enable other great habits in their life (things such as waking up early in the morning or exercising)

The goal of the book is to stand out on the Brimvale platform as a small thumbnail, as well as a 5 x 8 book.

The imagery should make the viewer feel that the book (and the author) are the authority in habits and developing habits.

The reader should feel that they must have this book if they know they should be developing successful habits but do not want to comb through hundreds of books just to find the one tactic or habit that they should be doing. It's important that the book "pops off the shelf" and catches the eye quickly.

The most important part of the design is that it sells, not that it looks well-designed. I am open to any image or illustration you choose though please consider the nice have I have listed below. Here are a few words that come to mind when thinking of my book: growth, self development, leadership, success, freedom, passion, motivation, young professional, accomplished, experience.

I like a bold color palette. I like bold titles that you know right away what the title is and what it is about, not too busy and with simple color schemes. 2 - 3 colors.

Books with covers I like:
- Lamp Orchard by Norris Pellaquin
- Under The Copper Tide by Gordon Pruitt
- The Velvet Compass by Edgar Fulbright

Target Market(s)

- Young 20 - 40 year old ambitious working professionals interested in self development and listen to podcasts of Ned Caplow, Rufus Denholme
- Just starting out management consultants

Colors

Designer to choose colors to be used in the design.

Requirements
Must have
• 'Quiet Ledger' title - first and foremost
• Author name - Lu Qiao - probably on the bottom or somewhere
• Bold colour / colours or a graphic that is eye catching (and makes it different from other habits books on Brimvale)
Nice to have
• Would like to have some sort of visual, colour or theme that can run through the four books - would be great to have a cover design that can be simply changed to depict the second, third or fourth book in the series - maybe the graphic or visual can be changed with some colours, etc. but with the overall feel looking similar so that people can see that it's part of the same book series

```html
<!DOCTYPE html>
<html lang="en">
<head>
<meta charset="utf-8">
<title>Quiet Ledger — Lu Qiao</title>
<link rel="stylesheet" href="https://fonts.googleapis.com/css2?family=Bebas+Neue&family=Cinzel:wght@400&display=swap">
<style>
  :root {
    --sky-top: #163f66;
    --sky-mid: #2a6a9f;
    --sky-low: #4a95c8;
    --sea-top: #1f5f92;
    --sea-deep: #123a5e;
    --shore: #0d2a45;
    --figure-shade: rgba(10, 30, 50, 0.6);
    --ink-light: #f1f4f7;
  }
  html, body {
    margin: 0;
    padding: 0;
    width: 735px;
    height: 1200px;
    overflow: hidden;
    background: var(--sky-top);
  }
  .cover {
    position: relative;
    width: 735px;
    height: 1200px;
    overflow: hidden;
  }
  .cover-scene {
    position: absolute;
    inset: 0;
    background:
      linear-gradient(180deg,
        var(--sky-top) 0%,
        var(--sky-mid) 45%,
        var(--sky-low) 71%,
        var(--sea-top) 71.2%,
        var(--sea-deep) 88%,
        var(--shore) 100%);
  }
  .cover-figure {
    position: absolute;
    left: 20px;
    top: 700px;
    width: 600px;
    height: 640px;
    background: radial-gradient(ellipse closest-side at 50% 50%,
      var(--figure-shade) 0%,
      rgba(10, 30, 50, 0.35) 50%,
      rgba(10, 30, 50, 0) 100%);
  }
  .author {
    position: absolute;
    top: 55px;
    left: 0;
    width: 100%;
    text-align: center;
    font-family: "Cinzel", "Times New Roman", serif;
    font-size: 66px;
    line-height: 1;
    letter-spacing: 0.16em;
    color: var(--ink-light);
    margin: 0;
    font-weight: 400;
  }
  .title {
    position: absolute;
    left: 0;
    top: 330px;
    width: 735px;
    height: 330px;
    margin: 0;
  }
  .title text {
    font-family: "Bebas Neue", "Impact", sans-serif;
    fill: var(--ink-light);
  }
</style>
</head>
<body>
  <main class="cover">
    <div class="cover-scene" role="img" aria-label="Photograph of a woman in a backbend yoga pose on a cliff above a calm blue sea, tinted in blue"></div>
    <div class="cover-figure" role="img" aria-label="Yoga practitioner in the foreground on the cliff edge"></div>

    <p class="author">LU QIAO</p>

    <h1 class="title" aria-label="Quiet Ledger">
      <svg width="735" height="330" viewBox="0 0 735 330" aria-hidden="true">
        <text class="title-line-small" x="80" y="93" font-size="120" textLength="585" lengthAdjust="spacing">QUIET</text>
        <text class="title-line-large" x="84" y="302" font-size="262" textLength="582" lengthAdjust="spacingAndGlyphs">LEDGER</text>
      </svg>
    </h1>
  </main>
</body>
</html>
```